Mardi Gras Ball 2014

We're looking to create an 8 1/2" x11" print design using certain elements that we provide.

This is for an invitation/program cover for a Mardi Gras Ball - so the design has to have a classy look using a set number of colors - GOLD, PURPLE, GREEN - white can also be used as accent or boarder elements.

Please use the file KPLOR 2014 for inspiration and direction. The design MUST connect to that file.

The final design should cause a WOW! factor and play off / or be a companion to design we will upload. (see files)

Requirements
Must have
• Dimension size 8 1/2'' x 11'' (bleed to the end)
Port Elvany Seal to remain (can be small)
A Mardi Gras Mask or person in mask behind front elements which should use transparency
Event location, date, time
Files appropriate for printing - with a semi-transparent object in file
Nice to have
• Key elements like shown on the KPLOR 2014 file
Purple as a key color - either as background or like feathers on picture
10th Annual must show nicely
FONTS: New Century Schoolbook LT and Spinwerad

```html
<!DOCTYPE html>
<html lang="en">
<head>
<meta charset="utf-8">
<title>Port Elvany Alumni — 10th Annual Mardi Gras Ball</title>
<link rel="stylesheet" href="https://fonts.googleapis.com/css2?family=Old+Standard+TT:wght@700&family=PT+Serif:ital,wght@0,700;1,700&display=swap">
<style>
  :root {
    --purple-deep: #3d12a8;
    --purple: #6b26c4;
    --purple-silk: #9a3fd6;
    --green: #0f7a3c;
    --green-deep: #0e4d47;
    --gold: #c99a35;
    --gold-light: #e2b95a;
    --cream: #efe2c6;
    --white: #ffffff;
    --outline: #4a1d7a;
  }
  * { margin: 0; padding: 0; box-sizing: border-box; }
  html, body { width: 928px; height: 1200px; overflow: hidden; background: var(--white); }
  .invitation {
    position: relative;
    width: 928px;
    height: 1200px;
    overflow: hidden;
    font-family: "PT Serif", serif;
    color: var(--white);
  }
  .backdrop {
    position: absolute; inset: 0;
    background:
      radial-gradient(ellipse 420px 300px at 620px 330px, rgba(190,110,240,.55), transparent 70%),
      radial-gradient(ellipse 380px 420px at 760px 760px, rgba(60,60,190,.55), transparent 70%),
      radial-gradient(ellipse 260px 220px at 560px 940px, rgba(150,160,40,.45), transparent 70%),
      linear-gradient(180deg, var(--purple-deep) 0%, var(--purple) 28%, var(--purple-silk) 42%, #4b3aa8 62%, var(--green) 80%, var(--green-deep) 100%);
  }
  .mask-photo {
    position: absolute;
    left: 0; top: 360px;
    width: 420px; height: 470px;
    border-radius: 0 200px 200px 0 / 0 240px 240px 0;
    background: linear-gradient(180deg, #b9862e 0%, var(--gold) 30%, #d8b978 50%, var(--cream) 72%, #cfc4a6 100%);
    -webkit-mask-image: linear-gradient(180deg, #000 75%, transparent 100%);
            mask-image: linear-gradient(180deg, #000 75%, transparent 100%);
  }
  .org-mark {
    position: absolute;
    left: 115px; top: 70px;
    width: 190px;
    text-align: center;
    font-family: "Old Standard TT", serif;
    font-size: 64px;
    font-weight: 700;
    color: var(--gold-light);
    letter-spacing: 2px;
  }
  .org-name {
    position: absolute;
    left: 30px; top: 204px;
    width: 390px;
    text-align: center;
    font-weight: 700;
    font-size: 27px;
    line-height: 40px;
  }
  .headline { position: absolute; left: 0; top: 0; }
  .headline text { font-family: "Old Standard TT", serif; font-weight: 700; paint-order: stroke; stroke-linejoin: round; }
  .headline .request { font-family: "PT Serif", serif; font-style: italic; font-size: 21px; fill: var(--white); }
  .big-white { fill: var(--white); stroke: var(--gold); stroke-width: 3px; }
  .big-gold { fill: var(--gold); stroke: var(--white); stroke-width: 3px; }
  .gras { fill: var(--white); stroke: var(--outline); stroke-width: 4px; }
  .event-details {
    position: absolute;
    left: 50px; top: 833px;
    width: 400px;
    text-align: center;
    font-weight: 700;
  }
  .event-day { font-size: 34px; line-height: 44px; }
  .event-date { font-size: 27px; line-height: 42px; }
  .event-time { font-size: 27px; line-height: 42px; }
  .venue-name { font-size: 21px; line-height: 32px; margin-top: 18px; }
  .venue-hall { font-size: 25px; line-height: 32px; }
  .venue-street { font-size: 20px; line-height: 32px; margin-top: 14px; letter-spacing: -.4px; }
  .venue-city { font-size: 28px; line-height: 36px; }
  .school-seal {
    position: absolute;
    left: 568px; top: 938px;
    width: 184px; height: 184px;
    border-radius: 50%;
    background: var(--purple);
    border: 5px solid var(--gold);
    display: flex; align-items: center; justify-content: center;
    text-align: center;
    font-weight: 700;
    font-size: 24px;
    line-height: 30px;
    color: var(--gold-light);
  }
</style>
</head>
<body>
<main class="invitation">
  <div class="backdrop" role="img" aria-label="Draped purple satin with a strand of pearls, fading into green and blue Mardi Gras masks"></div>
  <div class="mask-photo" role="img" aria-label="Photograph of an ornate gold Venetian carnival mask"></div>

  <div class="org-mark">KPLOR</div>
  <p class="org-name">THE ASSOCIATION OF<br>PORT ELVANY ALUMNI</p>

  <svg class="headline" width="928" height="1200" viewBox="0 0 928 1200" aria-label="10th Annual Mardi Gras Ball">
    <text class="request" x="688" y="247" text-anchor="middle">requests your presence at our</text>
    <text class="big-white" x="520" y="432" font-size="170" textLength="210" lengthAdjust="spacingAndGlyphs">10</text>
    <text class="big-white" x="735" y="358" font-size="82">th</text>
    <text class="big-gold" x="670" y="514" font-size="72" text-anchor="middle" textLength="340" lengthAdjust="spacingAndGlyphs">ANNUAL</text>
    <text class="big-gold" x="622" y="648" font-size="124" text-anchor="middle" textLength="450" lengthAdjust="spacingAndGlyphs">MARDI</text>
    <text class="gras" x="642" y="755" font-size="124" text-anchor="middle" textLength="405" lengthAdjust="spacingAndGlyphs">GRAS</text>
    <text class="big-gold" x="672" y="850" font-size="124" text-anchor="middle" textLength="345" lengthAdjust="spacingAndGlyphs">BALL</text>
  </svg>

  <section class="event-details">
    <p class="event-day">SATURDAY</p>
    <p class="event-date">FEBRUARY 22, 2014</p>
    <p class="event-time">7PM - 12AM</p>
    <p class="venue-name">HARLOW GRAND</p>
    <p class="venue-hall">CONVENTION CENTER</p>
    <p class="venue-street">2400 Meridian Hall Concourse</p>
    <p class="venue-city">MARLOWE, GEORGIA</p>
  </section>

  <div class="school-seal">Port<br>Elvany</div>
</main>
</body>
</html>
```